Redesign Website for Tandara Flame

I have an existing website on https://www.tandaraflame-example.com.au/ and would like to have this redesigned professionally with new content (please refer to word document). We are fire protection engineers providing fire services design expertise and engineering design to a range of different clients.

We also provide drafting services to clients in the form of completing final commissioning documentation such as 'as-installed' drawings and fire services block plans to ensure compliance with the building code and relevant Australian Standards.

Target Market(s)

Builders, Architects, Consultants, Project Managers

Industry/Entity Type

Engineering Consultant

Coding

Coded - Design and coding required

Number of Pages Required

4 page

Font styles to use
Sans Serif

Requirements
Must have
• Home and about Page, fire services design page, fire block plans page, contact us page (4 Pages).

The website colour choice must match or compliment the new company logo.
Nice to have
• Quality photos of fire services installations in buildings to Australian Standards.

A website similar to this would be ideal http://corbellpyro-example.com.au
Should not have
• Stolen licensed photos

```html
<!DOCTYPE html>
<html lang="en">
<head>
<meta charset="utf-8">
<title>Contact Us – Tandara Flame</title>
<link href="https://fonts.googleapis.com/css2?family=Outfit:wght@300;400;500;600&family=Tinos:wght@700&display=swap" rel="stylesheet">
<style>
  :root {
    --orange: #f7931e;
    --ink: #1e1e1e;
    --muted: #555;
    --line: #c9c9c9;
    --white: #ffffff;
    --mist: #eeeff0;
    --footer: #2b2d31;
    --footer-text: #d8d8d8;
    --hero-a: #8e8f8c;
    --hero-b: #c7c8c4;
  }
  * { box-sizing: border-box; margin: 0; padding: 0; }
  html, body { width: 720px; height: 1200px; overflow: hidden; }
  body { position: relative; background: var(--white); font-family: "Outfit", sans-serif; color: var(--ink); }
  .abs { position: absolute; }

  /* header */
  .site-nav { left: 0; top: 0; width: 720px; height: 48px; background: var(--white); z-index: 2; }
  .nav-link { top: 19px; font-size: 9px; color: var(--ink); text-decoration: none; transform: translateX(-50%); white-space: nowrap; }
  .logo-tab { left: 298px; top: 40px; z-index: 3; }
  .brand-name { left: 0; width: 720px; top: 45px; text-align: center; font-size: 10.5px; font-weight: 500; color: var(--orange); letter-spacing: .3px; z-index: 4; }
  .brand-dot { left: 353px; top: 20px; width: 14px; height: 14px; border-radius: 50%; background: var(--orange); z-index: 4; }

  /* hero */
  .hero { left: 0; top: 48px; width: 720px; height: 225px; background: linear-gradient(100deg, var(--hero-a), var(--hero-b) 70%, #dcdcda); }
  .hero-title { left: 0; width: 720px; top: 150px; text-align: center; font-family: "Tinos", serif; font-weight: 700; font-size: 22px; color: var(--white); }

  /* divider */
  .divider { left: 319px; width: 82px; height: 16px; }

  /* intro & form */
  .intro { left: 115px; width: 490px; top: 347px; text-align: center; font-size: 12.6px; line-height: 21.6px; }
  .field { border: 1px solid var(--line); background: var(--white); font-size: 7.6px; color: var(--ink); padding: 12px 12px; }
  .submit-btn { left: 297px; top: 644px; }

  /* contact information */
  .info-band { left: 0; top: 717px; width: 720px; height: 318px; background: var(--mist); }
  .info-title { left: 0; width: 720px; top: 756px; text-align: center; font-family: "Tinos", serif; font-weight: 700; font-size: 20px; }
  .info-card { top: 828px; width: 170px; text-align: center; transform: translateX(-50%); }
  .info-card svg { display: block; margin: 0 auto; }
  .info-heading { margin-top: 14px; font-family: "Tinos", serif; font-weight: 700; font-size: 13px; }
  .info-text { margin-top: 6px; font-size: 8.6px; line-height: 12.5px; color: #333; }

  /* footer */
  .site-footer { left: 0; top: 1035px; width: 720px; height: 165px; background: var(--footer); color: var(--footer-text); }
  .footer-brand { left: 110px; width: 110px; top: 1094px; text-align: center; font-size: 10px; font-weight: 500; color: var(--orange); }
  .footer-brand-dot { left: 157px; top: 1072px; width: 16px; height: 16px; border-radius: 50%; background: var(--orange); }
  .social { top: 1117px; width: 16px; height: 16px; border: 1px solid var(--white); border-radius: 50%; }
  .col-title { top: 1070px; font-family: "Tinos", serif; font-weight: 700; font-size: 7.6px; color: var(--white); }
  .col-rule { top: 1088px; width: 24px; height: 1px; background: var(--orange); }
  .col-links { top: 1096px; list-style: none; font-size: 6.3px; line-height: 13.4px; font-weight: 300; color: var(--white); }
  .newsletter { left: 479px; top: 1104px; }
  .footer-rule { left: 110px; top: 1173px; width: 500px; height: 1px; background: #55575b; }
  .copyright { left: 110px; top: 1182px; font-size: 6px; font-weight: 300; color: #b5b5b5; }
  .legal { right: 110px; top: 1182px; font-size: 6px; font-weight: 300; color: #b5b5b5; }
</style>
</head>
<body>

<header>
  <nav class="abs site-nav" aria-label="Main">
    <a class="abs nav-link" href="#" style="left:175px">Home</a>
    <a class="abs nav-link" href="#" style="left:248px">Fire Services</a>
    <a class="abs nav-link" href="#" style="left:472px">Fire Block Plans</a>
    <a class="abs nav-link" href="#" style="left:561px">Contact Us</a>
  </nav>
  <svg class="abs logo-tab" width="124" height="22" viewBox="0 0 124 22" aria-hidden="true">
    <polygon points="0,8 124,8 112,21 12,21" fill="#ffffff"/>
  </svg>
  <span class="abs brand-dot" aria-hidden="true"></span>
  <div class="abs brand-name">TANDARA FLAME</div>
</header>

<section>
  <div class="abs hero" role="img" aria-label="Photo of an underground car park with concrete columns and fire services pipework"></div>
  <h1 class="abs hero-title">Contact Us</h1>
</section>

<main>
  <svg class="abs divider" style="top:318px" viewBox="0 0 82 16" aria-hidden="true">
    <line x1="0" y1="8" x2="82" y2="8" stroke="#f7931e" stroke-width="1.4"/>
    <circle cx="41" cy="8" r="6.5" fill="#ffffff" stroke="#f7931e" stroke-width="1.4"/>
  </svg>

  <p class="abs intro">If you require assistance on any matters relating to fire services design or compliance of&nbsp; existing fire safety systems please fill in your details below and we will get in touch as soon as possible! Thank you!</p>

  <form>
    <div class="abs field" style="left:153px;top:428px;width:200px;height:30px">First Name</div>
    <div class="abs field" style="left:367px;top:428px;width:200px;height:30px">Last Name</div>
    <div class="abs field" style="left:153px;top:471px;width:200px;height:30px">Mobile Number</div>
    <div class="abs field" style="left:367px;top:471px;width:200px;height:30px">Email Address</div>
    <div class="abs field" style="left:153px;top:515px;width:414px;height:106px">Your Message</div>
    <svg class="abs submit-btn" width="126" height="28" viewBox="0 0 126 28" role="button" aria-label="Submit now">
      <polygon points="7,0 104,0 97,14 104,28 7,28 0,14" fill="#f7931e"/>
      <polygon points="104,1 119,1 125,14 119,27 104,27 98,14" fill="#ffffff" stroke="#f7931e" stroke-width="1.4"/>
      <circle cx="111.5" cy="14" r="5.5" fill="#f7931e"/>
      <text x="53" y="17.5" text-anchor="middle" font-family="Outfit, sans-serif" font-weight="600" font-size="8.4" fill="#ffffff">SUBMIT NOW!</text>
    </svg>
  </form>
</main>

<section>
  <div class="abs info-band" role="img" aria-label="Faded photo of a car park with fire technicians inspecting equipment"></div>
  <h2 class="abs info-title">Contact Information</h2>
  <svg class="abs divider" style="top:790px" viewBox="0 0 82 16" aria-hidden="true">
    <line x1="0" y1="8" x2="82" y2="8" stroke="#f7931e" stroke-width="1.4"/>
    <circle cx="41" cy="8" r="6.5" fill="#eeeff0" stroke="#f7931e" stroke-width="1.4"/>
  </svg>

  <div class="abs info-card" style="left:196px">
    <svg width="116" height="100" viewBox="0 0 116 100" aria-hidden="true">
      <polygon points="29,1 87,1 115,50 87,99 29,99 1,50" fill="none" stroke="#a8a8a8" stroke-width="1"/>
      <path d="M58 72 C50 62 40 54 40 44 A18 18 0 0 1 76 44 C76 54 66 62 58 72 Z" fill="none" stroke="#999" stroke-width="1.3"/>
      <circle cx="58" cy="44" r="12" fill="none" stroke="#f7931e" stroke-width="1.4"/>
      <polyline points="52,44 57,49 65,39" fill="none" stroke="#f7931e" stroke-width="1.6"/>
    </svg>
    <div class="info-heading">Location</div>
    <div class="info-text">Lorem ipsum dolor sit amet,<br>consectetur adipiscing elit, sed do</div>
  </div>

  <div class="abs info-card" style="left:360px">
    <svg width="116" height="100" viewBox="0 0 116 100" aria-hidden="true">
      <polygon points="29,1 87,1 115,50 87,99 29,99 1,50" fill="none" stroke="#a8a8a8" stroke-width="1"/>
      <rect x="45" y="27" width="26" height="43" rx="2" fill="none" stroke="#999" stroke-width="1.3"/>
      <rect x="48" y="31" width="20" height="33" fill="none" stroke="#bbb" stroke-width="0.8"/>
      <circle cx="67" cy="45" r="10" fill="#eeeff0" stroke="#f7931e" stroke-width="1.4"/>
      <path d="M63 41 q0 8 8 8 l1.5 -2 -2.5 -2 -1.5 1 q-2 -1 -3 -3 l1 -1.5 -2 -2.5 z" fill="none" stroke="#f7931e" stroke-width="1"/>
    </svg>
    <div class="info-heading">Mobile Number</div>
    <div class="info-text">+1234567890</div>
  </div>

  <div class="abs info-card" style="left:523px">
    <svg width="116" height="100" viewBox="0 0 116 100" aria-hidden="true">
      <polygon points="29,1 87,1 115,50 87,99 29,99 1,50" fill="none" stroke="#a8a8a8" stroke-width="1"/>
      <rect x="38" y="42" width="40" height="28" fill="none" stroke="#999" stroke-width="1.3"/>
      <polyline points="38,42 58,58 78,42" fill="none" stroke="#999" stroke-width="1.3"/>
      <line x1="38" y1="70" x2="53" y2="55" stroke="#999" stroke-width="1.1"/>
      <line x1="78" y1="70" x2="63" y2="55" stroke="#999" stroke-width="1.1"/>
      <circle cx="58" cy="37" r="9.5" fill="#eeeff0" stroke="#f7931e" stroke-width="1.4"/>
      <text x="58" y="41" text-anchor="middle" font-family="Outfit, sans-serif" font-size="11" fill="#f7931e">@</text>
    </svg>
    <div class="info-heading">Email Address</div>
    <div class="info-text">info@tandaraflame-example.com</div>
  </div>
</section>

<footer>
  <div class="abs site-footer" role="img" aria-label="Darkened photo of a car park interior"></div>
  <span class="abs footer-brand-dot" aria-hidden="true"></span>
  <div class="abs footer-brand">TANDARA FLAME</div>
  <span class="abs social" style="left:127px" aria-label="Social link"></span>
  <span class="abs social" style="left:146px" aria-label="Social link"></span>
  <span class="abs social" style="left:166px" aria-label="Social link"></span>
  <span class="abs social" style="left:186px" aria-label="Social link"></span>

  <div class="abs col-title" style="left:233px">Quick Links</div>
  <div class="abs col-rule" style="left:233px"></div>
  <ul class="abs col-links" style="left:233px">
    <li>Home</li><li>About Us</li><li>Fire Services</li><li>Fire Block Plans</li><li>Contact Us</li>
  </ul>

  <div class="abs col-title" style="left:309px">Fire Services</div>
  <div class="abs col-rule" style="left:309px"></div>
  <ul class="abs col-links" style="left:309px">
    <li>Smoke Alarms</li><li>Fire Hydrants</li><li>Emergency Lighting</li><li>Exit Signs</li><li>See All »</li>
  </ul>

  <div class="abs col-title" style="left:378px">Fire Block Plans</div>
  <div class="abs col-rule" style="left:378px"></div>
  <ul class="abs col-links" style="left:378px">
    <li>Zone Block Plan</li><li>Fire Hydrant Block Plans</li><li>Sprinkler Block Plans</li>
  </ul>

  <div class="abs col-title" style="left:479px">Subscribe Our Newsletter</div>
  <div class="abs col-rule" style="left:479px;width:37px"></div>
  <svg class="abs newsletter" width="124" height="21" viewBox="0 0 124 21" aria-label="Newsletter signup">
    <polygon points="5,0 119,0 124,10.5 119,21 5,21 0,10.5" fill="#ffffff"/>
    <polygon points="80,1 117,1 122,10.5 117,20 80,20 76,10.5" fill="#f7931e"/>
    <text x="12" y="13" font-family="Outfit, sans-serif" font-weight="300" font-size="6" fill="#888">Email...</text>
    <text x="99" y="13" text-anchor="middle" font-family="Tinos, serif" font-weight="700" font-size="6" fill="#ffffff">Subscribe!</text>
  </svg>

  <div class="abs footer-rule"></div>
  <div class="abs copyright">© Copyright Tandara Flame 2021, All Rights Reserved.</div>
  <div class="abs legal">Privacy Policy&nbsp; |&nbsp; Terms &amp; Conditions</div>
</footer>

</body>
</html>
```